Banner Design for Physiotherapy Business

I need a banner designed for a physiotherapy business. The word ‘Physiotherapy’ should be prominent at the top. I’ve attached a document outlining what text and a suggestion of a picture I’d like included. The photo I have suggested in the document won’t upload to artvolley though as the dimensions are too large. I am open to other photos being used though. I would like to see designs that use the colour orange (as seen in the example) or green preferrably. The dimensions need to be 841mm x 2055mm and provided in PDF, JPG, and PNG format and 300dpi in CMYK colour mode.

```html
<!DOCTYPE html>
<html lang="en">
<head>
<meta charset="utf-8">
<title>Physiotherapy Roll-up Banner</title>
<link href="https://fonts.googleapis.com/css2?family=Oswald:wght@300;400;700&family=Poppins:wght@600;700&display=swap" rel="stylesheet">
<style>
  :root {
    --blue: #0a6cb8;
    --blue-deep: #0b5ea6;
    --blue-light: #1a80cf;
    --blue-band: #1288d6;
    --slate: #4a4b50;
    --ink: #151515;
    --paper: #ffffff;
    --backdrop: #d9d9d9;
  }
  * { margin: 0; padding: 0; box-sizing: border-box; }
  html, body { width: 1200px; height: 1080px; overflow: hidden; }
  body { background: var(--backdrop); position: relative; font-family: "Oswald", sans-serif; }

  .banner {
    position: absolute; left: 390px; top: 27px;
    width: 420px; height: 1026px;
    background: var(--paper); overflow: hidden;
    box-shadow: 0 6px 18px rgba(0,0,0,.25);
  }
  .banner-shapes { position: absolute; inset: 0; width: 420px; height: 1026px; }

  .title {
    position: absolute; top: 0; left: 0; width: 420px; height: 110px;
    display: flex; align-items: center; justify-content: center;
    color: var(--paper); font-weight: 700; font-size: 57px; letter-spacing: 0.5px;
    padding-top: 8px;
  }

  .section-heading {
    position: absolute; left: 43px; top: 494px;
    font-size: 56px; line-height: 1; color: var(--ink);
    font-weight: 400; letter-spacing: 0; white-space: nowrap;
    transform: scaleX(0.95); transform-origin: left top;
  }
  .section-heading strong { color: var(--blue); font-weight: 700; }
  .heading-rule {
    position: absolute; left: 39px; top: 557px; width: 341px; height: 3px; background: var(--blue);
  }

  .treat-list { position: absolute; list-style: none; font-size: 17px; color: var(--ink); font-weight: 400; }
  .treat-list li { position: absolute; left: 0; padding-left: 20px; line-height: 23px; white-space: nowrap; }
  .treat-list li::before {
    content: ""; position: absolute; left: 0; top: 5px;
    width: 13px; height: 13px; border: 1.4px solid var(--blue); border-radius: 50%;
  }
  .treat-list li::after {
    content: ""; position: absolute; left: 4px; top: 8px;
    width: 3px; height: 5px; border-right: 1.4px solid var(--blue); border-bottom: 1.4px solid var(--blue);
    transform: rotate(40deg);
  }
  .treat-list.left { left: 37px; top: 572px; }
  .treat-list.right { left: 223px; top: 572px; }

  .member-mark {
    position: absolute; left: 37px; top: 872px;
    display: flex; align-items: center; gap: 10px;
    color: var(--blue); font-family: "Oswald", sans-serif; font-weight: 400;
    font-size: 12px; line-height: 1.25; text-transform: uppercase;
  }
  .member-mark .dot { width: 44px; height: 44px; border-radius: 50%; background: var(--blue); flex: none; }

  .appointment { position: absolute; left: 232px; top: 868px; width: 163px; }
  .appointment-tag {
    background: var(--blue); color: var(--paper);
    font-weight: 700; font-size: 15px; text-align: center; height: 23px; line-height: 23px;
  }
  .appointment-address {
    margin-top: 7px; padding-left: 8px;
    font-family: "Poppins", sans-serif; font-weight: 600; font-size: 10.5px; line-height: 14.5px; color: var(--ink);
  }

  .phone-pill {
    position: absolute; left: 31px; top: 947px; width: 357px; height: 50px;
    background: var(--paper); border: 3px solid var(--blue-band); border-radius: 25px;
    display: flex; align-items: center; justify-content: center; gap: 14px;
    font-family: "Poppins", sans-serif; font-weight: 700; font-size: 34px; color: var(--ink);
  }
  .phone-pill svg { width: 30px; height: 30px; }
</style>
</head>
<body>
  <main class="banner">
    <svg class="banner-shapes" viewBox="0 0 620 1515" preserveAspectRatio="none" role="img" aria-label="Photo: physiotherapist guiding an older man through a dumbbell arm exercise in a bright clinic">
      <defs>
        <linearGradient id="photoTone" x1="0" y1="0" x2="1" y2="1">
          <stop offset="0" stop-color="#f1f3f5"/>
          <stop offset="0.5" stop-color="#dfe3e8"/>
          <stop offset="1" stop-color="#b9c3cf"/>
        </linearGradient>
      </defs>
      <polygon points="0,163 620,163 620,597 338,512 0,557" fill="url(#photoTone)"/>
    </svg>
    <svg class="banner-shapes" viewBox="0 0 620 1515" preserveAspectRatio="none" aria-hidden="true">
      <rect x="0" y="0" width="620" height="163" fill="var(--blue)"/>
      <rect x="0" y="1437" width="620" height="78" fill="var(--blue-band)"/>
      <polygon points="0,557 218,719 300,578 0,557" fill="var(--slate)"/>
      <polygon points="218,719 338,512 458,627" fill="var(--blue-deep)"/>
      <polygon points="338,512 620,597 620,782 458,627" fill="var(--blue-light)"/>
    </svg>

    <h1 class="title">PHYSIOTHERAPY</h1>

    <h2 class="section-heading">WHAT WE <strong>TREAT</strong></h2>
    <div class="heading-rule"></div>

    <ul class="treat-list left">
      <li style="top:0">Arthritis</li>
      <li style="top:31px">Sciatic pain</li>
      <li style="top:64px">Repetitive strain injuries</li>
      <li style="top:97px">Tennis elbow</li>
      <li style="top:127px">Postural pain</li>
      <li style="top:160px">Workplace injuries</li>
      <li style="top:193px">Motor vehicle accidents</li>
      <li style="top:223px">Women’s health issues</li>
      <li style="top:254px">Clinical exercise</li>
    </ul>
    <ul class="treat-list right">
      <li style="top:0">Back pain / Neck pain</li>
      <li style="top:29px">Sports injuries</li>
      <li style="top:58px">Post surgical<br>management (hip and<br>knee arthroscopes,<br>joint replacement<br>surgery)</li>
      <li style="top:178px">Shoulder pain and<br>dysfunction</li>
      <li style="top:229px">Pre-employment<br>functional assessments</li>
    </ul>

    <div class="member-mark">
      <span class="dot"></span>
      <span>Allied Physio<br>Network<br>Member</span>
    </div>

    <div class="appointment">
      <div class="appointment-tag">MAKE AN APPOINTMENT</div>
      <p class="appointment-address">Kestrel Family Practice<br>18-20 Wattle Ln<br>Hawthorn Vale VIC 3199</p>
    </div>

    <div class="phone-pill">
      <svg viewBox="0 0 24 24" fill="none" stroke="var(--blue)" stroke-width="1.6" stroke-linecap="round" stroke-linejoin="round" aria-hidden="true">
        <path d="M5 3.5h3l1.5 4-2 1.3a11 11 0 0 0 7.7 7.7l1.3-2 4 1.5v3a2 2 0 0 1-2.2 2A17 17 0 0 1 3 5.7 2 2 0 0 1 5 3.5z"/>
        <path d="M14 6.5a4 4 0 0 1 3.5 3.5M14 3a7.5 7.5 0 0 1 7 7"/>
      </svg>
      <span>(03) 9555 0142</span>
    </div>
  </main>
</body>
</html>
```